Breezeway Climate Business Card Design

Design new, 2 sides, business cards for a residential and light commercial heating, air conditioning contractor.

Target Market(s)

Homeowners, small businesses

Industry/Entity Type

Business

Contact Information for Business Card

Dominic Vasquerelli
Phone - 555-214-6837
Email
Address - PO box 618
Millbrook NJ 07999
Website - www.BreezewayClimateLLC.example

Requirements
Must have
• logo, company colors, standard size with no die cut, so I can use printhaven

```html
<!DOCTYPE html>
<html lang="en">
<head>
<meta charset="utf-8">
<title>Breezeway Climate Business Card</title>
<link rel="stylesheet" href="https://fonts.googleapis.com/css2?family=Open+Sans:wght@400;700&display=swap">
<style>
  :root {
    --backdrop: #e9e6e2;
    --card: #ffffff;
    --ink: #1a1a1a;
    --ink-soft: #222222;
    --card-shadow: rgba(0, 0, 0, 0.18);
  }
  html, body {
    margin: 0;
    padding: 0;
    width: 1200px;
    height: 1000px;
    overflow: hidden;
    background: var(--backdrop);
    font-family: "Open Sans", Arial, sans-serif;
    color: var(--ink);
  }
  .canvas {
    position: relative;
    width: 1200px;
    height: 1000px;
  }
  .card {
    position: absolute;
    left: 266px;
    width: 666px;
    height: 397px;
    background: var(--card);
    border-radius: 24px;
    box-shadow: 0 2px 8px var(--card-shadow);
  }
  .card--front { top: 74px; }
  .card--back { top: 533px; }

  .brand-name {
    position: absolute;
    margin: 0;
    text-align: center;
    font-weight: 700;
    color: var(--ink);
    line-height: 1.05;
    text-transform: uppercase;
    letter-spacing: 1px;
  }
  .card--front .brand-name {
    left: 38px;
    top: 148px;
    width: 283px;
    font-size: 38px;
  }
  .card--back .brand-name {
    left: 154px;
    top: 152px;
    width: 358px;
    font-size: 48px;
  }

  .contact {
    position: absolute;
    left: 358px;
    top: 102px;
  }
  .contact__name {
    margin: 0;
    font-size: 17px;
    font-weight: 700;
    line-height: 22px;
    letter-spacing: 0.2px;
  }
  .contact__title {
    margin: 0;
    font-size: 16px;
    line-height: 22px;
    color: var(--ink-soft);
  }
  .contact__company {
    margin: 15px 0 0;
    font-size: 15px;
    font-weight: 700;
    line-height: 23px;
  }
  .contact__address {
    margin: 0;
    font-size: 16px;
    line-height: 24px;
    color: var(--ink-soft);
  }
  .contact__list {
    list-style: none;
    margin: 14px 0 0;
    padding: 0;
  }
  .contact__item {
    display: flex;
    align-items: center;
    gap: 8px;
    font-size: 16px;
    line-height: 23px;
    color: var(--ink-soft);
  }
  .contact__icon {
    width: 14px;
    height: 14px;
    flex: none;
    fill: var(--ink);
  }
</style>
</head>
<body>
<main class="canvas">
  <section class="card card--front" aria-label="Business card front">
    <p class="brand-name">Breezeway<br>Climate</p>
    <div class="contact">
      <p class="contact__name">Dominic Vasquerelli</p>
      <p class="contact__title">Vice President</p>
      <p class="contact__company">Breezeway Climate LLC</p>
      <p class="contact__address">PO box 618 Millbrook NJ 07999</p>
      <ul class="contact__list">
        <li class="contact__item">
          <svg class="contact__icon" viewBox="0 0 16 16" aria-hidden="true"><path d="M2 5c0-2 3-3 6-3s6 1 6 3v1h-3V4.5C10 4 6 4 5 4.5V6H2z"/><path d="M4 7h8l2 6H2z"/></svg>
          <span>555-214-6837</span>
        </li>
        <li class="contact__item">
          <svg class="contact__icon" viewBox="0 0 16 16" aria-hidden="true"><path d="M1 3h14v10H1z"/><path d="M1 3l7 6 7-6" fill="none" stroke="#fff" stroke-width="1.4"/></svg>
          <span>info@breezewayclimatellc.example</span>
        </li>
        <li class="contact__item">
          <svg class="contact__icon" viewBox="0 0 16 16" aria-hidden="true"><circle cx="8" cy="8" r="7"/><path d="M1 8h14M8 1c-3 3-3 11 0 14M8 1c3 3 3 11 0 14" fill="none" stroke="#fff" stroke-width="1.1"/></svg>
          <span>www.breezewayclimatellc.example</span>
        </li>
      </ul>
    </div>
  </section>

  <section class="card card--back" aria-label="Business card back">
    <p class="brand-name">Breezeway<br>Climate</p>
  </section>
</main>
</body>
</html>
```